Hip Music Management Co. BIz Card

I have a logo (attached) the back side of the card should the full logo on the entire card- that's it. The front side of the card should show the logo somewhere, keeping with the 4 different shades of blue. The front side of the card can be a white background with logo and colored typeface for all info. Pretty simple.

Target Market(s)

I manage and produce a whole bunch of major label and indie artists.

Industry/Entity Type

Management

Contact Information for Business Card

Velmora Sound House (logo)
Dale Fornwick
President
www.velmorasoundhouse.com
dale@velmorasoundhouse.com
+1 310.555.7182
418 Willow Bend Lane
Ashgrove Falls, NY 10599

Requirements
Must have
• Entire logo on back side. White background on front- unless you provide something more interesting.
Nice to have
• On the front of the card if you choose a white backgound, if possible take my logo without the blue background (over white) that would be cool.

```html
<!DOCTYPE html>
<html lang="en">
<head>
<meta charset="utf-8">
<title>Velmora Sound House – Business Card</title>
<link href="https://fonts.googleapis.com/css2?family=Arimo:ital,wght@0,400;0,700;1,400&display=swap" rel="stylesheet">
<style>
  :root {
    --backdrop: #b4b0b1;
    --navy: #19214d;
    --sky: #3fa6e0;
    --teal: #1fb6d4;
    --ink-blue: #1c86cf;
    --white: #ffffff;
    --font-text: "Arimo", Arial, sans-serif;
  }
  * { margin: 0; padding: 0; box-sizing: border-box; }
  html, body {
    width: 1200px;
    height: 900px;
    overflow: hidden;
    background: var(--backdrop);
    font-family: var(--font-text);
  }
  .canvas { position: relative; width: 1200px; height: 900px; }

  .card {
    position: absolute;
    width: 640px;
    height: 366px;
    overflow: hidden;
  }

  /* Back side */
  .card--back {
    left: 90px;
    top: 70px;
    background: var(--navy);
    display: flex;
    align-items: center;
    justify-content: center;
  }
  .brand-name--back {
    font-family: var(--font-text);
    font-weight: 700;
    font-size: 44px;
    letter-spacing: 1px;
    color: var(--sky);
  }

  /* Front side */
  .card--front {
    left: 470px;
    top: 464px;
    background: var(--white);
  }
  .brand-band {
    position: absolute;
    left: 0;
    top: 52px;
    width: 360px;
    height: 62px;
  }
  .brand-name--front {
    position: absolute;
    left: 40px;
    top: 66px;
    font-family: var(--font-text);
    font-weight: 700;
    font-size: 27px;
    letter-spacing: 0.5px;
    color: var(--sky);
    white-space: nowrap;
  }
  .person {
    position: absolute;
    left: 40px;
    top: 134px;
  }
  .person__name {
    font-size: 22px;
    color: var(--ink-blue);
    font-weight: 400;
  }
  .person__title {
    margin-top: 6px;
    font-size: 14px;
    font-style: italic;
    color: var(--navy);
  }
  .contact-list {
    position: absolute;
    left: 36px;
    top: 222px;
    list-style: none;
  }
  .contact-list__item {
    display: flex;
    align-items: center;
    gap: 9px;
    height: 25px;
    font-size: 15px;
    color: var(--ink-blue);
  }
  .contact-list__icon {
    width: 14px;
    height: 14px;
    flex: none;
    fill: var(--teal);
  }
  .accent-bar {
    position: absolute;
    right: 0;
    bottom: 34px;
    width: 170px;
    height: 16px;
  }
</style>
</head>
<body>
<main class="canvas">

  <section class="card card--back" aria-label="Card back">
    <span class="brand-name--back">Velmora Sound House</span>
  </section>

  <section class="card card--front" aria-label="Card front">
    <svg class="brand-band" viewBox="0 0 360 62" aria-hidden="true">
      <polygon points="0,0 360,0 322,62 0,62" fill="var(--navy)"/>
    </svg>
    <span class="brand-name--front">Velmora Sound House</span>

    <div class="person">
      <p class="person__name">Dale Fornwick</p>
      <p class="person__title">President</p>
    </div>

    <ul class="contact-list">
      <li class="contact-list__item">
        <svg class="contact-list__icon" viewBox="0 0 16 16" aria-hidden="true">
          <circle cx="8" cy="8" r="7"/>
          <path d="M8 1v14M1 8h14M3 4.5h10M3 11.5h10" stroke="#fff" stroke-width="1" fill="none"/>
        </svg>
        www.velmorasoundhouse.com
      </li>
      <li class="contact-list__item">
        <svg class="contact-list__icon" viewBox="0 0 16 16" aria-hidden="true">
          <rect x="1" y="3" width="14" height="10"/>
          <path d="M1 3l7 6 7-6" stroke="#fff" stroke-width="1.2" fill="none"/>
        </svg>
        dale@velmorasoundhouse.com
      </li>
      <li class="contact-list__item">
        <svg class="contact-list__icon" viewBox="0 0 16 16" aria-hidden="true">
          <path d="M4 1l2.5 3.5-1.5 1.5c.8 2 2.5 3.7 4.5 4.5l1.5-1.5L14.5 11.5 12.5 14C7 13.5 2.5 9 2 3.5z"/>
        </svg>
        +1 310.555.7182 418
      </li>
      <li class="contact-list__item">
        <svg class="contact-list__icon" viewBox="0 0 16 16" aria-hidden="true">
          <path d="M8 1L0.5 8H3v7h4v-4h2v4h4V8h2.5z"/>
        </svg>
        Willow Bend Lane Ashgrove Falls, NY 10599
      </li>
    </ul>

    <svg class="accent-bar" viewBox="0 0 170 16" aria-hidden="true">
      <defs>
        <linearGradient id="accentFade" x1="0" x2="1" y1="0" y2="0">
          <stop offset="0" stop-color="var(--teal)"/>
          <stop offset="0.55" stop-color="var(--navy)"/>
          <stop offset="1" stop-color="var(--navy)"/>
        </linearGradient>
      </defs>
      <polygon points="14,0 170,0 170,16 0,16" fill="url(#accentFade)"/>
    </svg>
  </section>

</main>
</body>
</html>
```